Business Card Design Project

We are an agricultural business based in Brisbane.
We design, manage and operate regional saleyards. Our logo is green/silver in colour and details of our business can be found on our website www.vodemarketyards.com.au

Just wanting a corporate design for some business cards and include name, position, contact details.

Thanks

Industry/Entity Type

Business

```html
<!DOCTYPE html>
<html lang="en">
<head>
<meta charset="utf-8">
<title>Vode Market Yards – Business Card</title>
<link rel="stylesheet" href="https://fonts.googleapis.com/css2?family=Arimo:wght@400;700&display=swap">
<style>
  :root {
    --paper: #ffffff;
    --card-tint: #e9f3e6;
    --swirl-tone: #cfe2ca;
    --ink: #111111;
    --rule: #000000;
    --brand-green: #0c8843;
  }
  html, body {
    margin: 0;
    padding: 0;
    width: 1200px;
    height: 743px;
    overflow: hidden;
    background: var(--paper);
  }
  .card {
    position: relative;
    width: 1200px;
    height: 743px;
    overflow: hidden;
    background: var(--paper);
    font-family: "Arimo", Arial, sans-serif;
    color: var(--ink);
  }
  .top-rule {
    position: absolute;
    left: 34px; top: 3px;
    width: 1162px; height: 13px;
    background: var(--rule);
  }
  .tint-panel {
    position: absolute;
    left: 34px; top: 16px;
    width: 1162px; height: 624px;
    background: var(--card-tint);
  }
  .swirl-area {
    position: absolute;
    left: 34px; top: 16px;
    width: 340px; height: 624px;
    background: linear-gradient(90deg, var(--swirl-tone) 0%, rgba(207,226,202,0.55) 55%, rgba(233,243,230,0) 100%);
  }
  .bottom-rule {
    position: absolute;
    left: 34px; top: 640px;
    width: 1162px; height: 20px;
    background: var(--rule);
  }
  .bottom-band {
    position: absolute;
    left: 34px; top: 666px;
    width: 1162px; height: 71px;
    background: var(--brand-green);
  }
  .brand-name {
    position: absolute;
    left: 390px; top: 78px;
    width: 520px;
    margin: 0;
    text-align: center;
    font-weight: 700;
    font-size: 46px;
    line-height: 54px;
    letter-spacing: 0.5px;
    color: var(--ink);
  }
  .contact__person,
  .contact__reach {
    position: absolute;
    font-size: 32px;
    line-height: 46px;
    white-space: nowrap;
  }
  .contact__person p,
  .contact__reach p { margin: 0; }
  .contact__person { left: 373px; }
  .contact__reach { right: 57px; text-align: right; }
  .contact--first .contact__person,
  .contact--first .contact__reach { top: 296px; }
  .contact--second .contact__person,
  .contact--second .contact__reach { top: 478px; }
  .contact__role { font-weight: 700; }
</style>
</head>
<body>
  <main class="card">
    <div class="top-rule"></div>
    <div class="tint-panel"></div>
    <div class="swirl-area" role="img" aria-label="Soft pale green leafy swirl ornament along the left edge"></div>

    <h1 class="brand-name">VODE MARKET<br>YARDS</h1>

    <section class="contact contact--first">
      <div class="contact__person">
        <p class="contact__name">Daniel Hartley</p>
        <p class="contact__role">General Manager</p>
        <p class="contact__company">VMY</p>
      </div>
      <div class="contact__reach">
        <p class="contact__email">daniel@vodemarketyards.com.au</p>
        <p class="contact__phone">Phone:0491570156</p>
      </div>
    </section>

    <section class="contact contact--second">
      <div class="contact__person">
        <p class="contact__name">Mark Fenwick</p>
        <p class="contact__role">Managing Director</p>
        <p class="contact__company">VMY</p>
      </div>
      <div class="contact__reach">
        <p class="contact__email">mark@vodemarketyards.com.au</p>
      </div>
    </section>

    <div class="bottom-rule"></div>
    <div class="bottom-band"></div>
  </main>
</body>
</html>
```